OSKA Dispatch (e-update) Design

Using Constant Contact, we need a template news email designed that we can re-use on a regular basis. Our news email would feature an average of 10 content blocks and would love the chance to feature photos with at least 8 of the content blocks. Whatever is designed would need to be transferrable to our constant contact account. Our news content per news item is short, usually a paragraph with links back to our site and events. The template would need a banner that really showcases the email design or helps brand the email. We are looking for a design that is sophisticated but youthful. We recently rebranded our firm and are great with the use of our new corporate colors.

Target Market(s)

Our association members of 700 professional real estate managers of highrises and buildings.

Colors

Designer to choose colors to be used in the design.

Requirements
Must have
• Email template design in Constant Contact to include a banner, area for 8 to 10 content blocks with cooresponding photos. A sophisticated and colorful design that makes people want to read the content.
Should not have
• Clip art

```html
<!DOCTYPE html>
<html lang="en">
<head>
<meta charset="utf-8">
<title>OSKA Dispatch</title>
<link href="https://fonts.googleapis.com/css2?family=Lato:wght@900&family=Open+Sans:wght@400;600;700&display=swap" rel="stylesheet">
<style>
  :root {
    --frame: #000000;
    --white: #ffffff;
    --magenta: #b0246f;
    --navy: #3c4a7d;
    --ink: #111111;
    --body: #333333;
    --button-blue: #6674bb;
    --yellow: #f7c51e;
    --mist: #eeeeee;
    --footer: #4d4d4d;
  }
  * { box-sizing: border-box; margin: 0; padding: 0; }
  html, body {
    width: 1200px; height: 3321px; overflow: hidden;
    background: var(--frame);
    font-family: "Open Sans", Arial, sans-serif;
  }
  .newsletter {
    position: absolute; left: 44px; top: 49px;
    width: 1107px; height: 3234px;
    background: var(--white);
  }
  /* Header */
  .masthead {
    height: 148px;
    display: flex; align-items: center; justify-content: center;
  }
  .brand-name {
    font-size: 40px; font-weight: 600; line-height: 1; color: var(--navy);
    letter-spacing: 0.5px;
  }
  /* Hero */
  .hero {
    position: relative; height: 567px;
    background: linear-gradient(100deg, var(--magenta) 0%, #b73c7c 55%, #a9487f 100%);
    color: var(--white);
  }
  .hero-content { position: absolute; left: 93px; top: 178px; width: 720px; }
  .hero-title {
    font-family: "Lato", Arial, sans-serif; font-weight: 900;
    font-size: 54px; line-height: 1; letter-spacing: 0.5px;
  }
  .hero-text { margin-top: 22px; font-size: 19.5px; line-height: 27px; }
  .btn {
    display: inline-flex; align-items: center; justify-content: center;
    width: 138px; height: 45px;
    font-size: 15px; font-weight: 700; letter-spacing: 0.5px;
    text-decoration: none; text-transform: uppercase;
  }
  .btn-yellow { margin-top: 20px; background: var(--yellow); color: var(--ink); }
  .btn-blue { background: var(--button-blue); color: var(--white); }
  /* Intro paragraph */
  .intro { padding-top: 34px; text-align: center; }
  .intro-title { font-size: 37px; font-weight: 700; color: var(--navy); line-height: 46px; }
  .intro-text {
    width: 900px; margin: 14px auto 0;
    font-size: 16.5px; line-height: 29px; color: var(--body);
  }
  /* Article grid */
  .articles {
    position: absolute; left: 95px; top: 936px;
    display: grid; grid-template-columns: 437px 437px; column-gap: 44px;
    grid-auto-rows: 411px; row-gap: 30px;
  }
  .article-photo {
    width: 437px; height: 189px;
    background: linear-gradient(180deg, #8fb6d9 0%, #b9cfe0 42%, #b99c82 60%, #6f9a4a 100%);
  }
  .article-title {
    margin-top: 31px; font-size: 24px; font-weight: 700; color: var(--ink);
    line-height: 30px; letter-spacing: 0.3px;
  }
  .article-text {
    margin-top: 12px; font-size: 17.5px; line-height: 27px; color: var(--body);
    white-space: nowrap;
  }
  .article .btn { margin-top: 22px; }
  /* Closing band */
  .closing {
    position: absolute; left: 0; top: 2674px; width: 1107px; height: 299px;
    background: var(--mist); text-align: center;
  }
  .closing-title {
    margin-top: 54px; font-size: 43px; font-weight: 700; line-height: 51px;
    color: var(--magenta); letter-spacing: 0.5px;
  }
  .closing-text {
    width: 1000px; margin: 20px auto 0;
    font-size: 17.5px; line-height: 28px; color: var(--body);
  }
  /* Footer */
  .footer {
    position: absolute; left: 0; top: 2973px; width: 1107px; height: 261px;
    background: var(--footer); color: var(--white); text-align: center;
  }
  .social { display: flex; justify-content: center; gap: 20px; margin-top: 53px; }
  .social-dot { width: 40px; height: 40px; border-radius: 50%; background: var(--white); display: block; }
  .footer-text { margin-top: 24px; font-size: 17.5px; line-height: 27px; }
  .footer-links { margin-top: 26px; font-size: 17.5px; }
  .footer-links a { color: var(--white); text-decoration: none; }
  .footer-links .sep { margin: 0 8px; }
</style>
</head>
<body>
<main class="newsletter">
  <header class="masthead">
    <span class="brand-name">OSKA Dispatch</span>
  </header>

  <section class="hero" role="img" aria-label="Photo of a large suburban house tinted magenta">
    <div class="hero-content">
      <h1 class="hero-title">REAL ESTATE MARKET</h1>
      <p class="hero-text">Lorem ipsum dolor sit amet, consec tetuer adipi scing elit, sed diam nonummy<br>nibh euismod tincidunt ut laoreet dolore magna aliquam erat volutpat.</p>
      <a class="btn btn-yellow" href="#">View More</a>
    </div>
  </section>

  <section class="intro">
    <h2 class="intro-title">Paragraph Section Title Here</h2>
    <p class="intro-text">Lorem ipsum dolor sit amet, consectetuer adipiscing elit, sed diam nonummy nibh euismod tincidunt ut<br>laoreet dolore magna aliquam erat volutpat. Ut wisi enim ad minim veniam, quis nostrud.<br>Ut wisi enim ad minim veniam, quis ad nostrud.</p>
  </section>

  <section class="articles">
    <article class="article">
      <div class="article-photo" role="img" aria-label="Stone two-storey house with trees at dusk"></div>
      <h3 class="article-title">Section Block Title Here</h3>
      <p class="article-text">Lorem ipsum dolor sit amet, consec tetuer adipi<br>elit, sed diam nonummy nibh euismod tincidunt<br>ut laoreet dolore magna aliquam erat volutpat.</p>
      <a class="btn btn-blue" href="#">View More</a>
    </article>
    <article class="article">
      <div class="article-photo" role="img" aria-label="Single-storey cream house with green lawn"></div>
      <h3 class="article-title">Section Block Title Here</h3>
      <p class="article-text">Lorem ipsum dolor sit amet, consec tetuer adipi<br>elit, sed diam nonummy nibh euismod tincidunt<br>ut laoreet dolore magna aliquam erat volutpat.</p>
      <a class="btn btn-blue" href="#">View More</a>
    </article>
    <article class="article">
      <div class="article-photo" role="img" aria-label="Large stone house under blue sky"></div>
      <h3 class="article-title">Section Block Title Here</h3>
      <p class="article-text">Lorem ipsum dolor sit amet, consec tetuer adipi<br>elit, sed diam nonummy nibh euismod tincidunt<br>ut laoreet dolore magna aliquam erat volutpat.</p>
      <a class="btn btn-blue" href="#">View More</a>
    </article>
    <article class="article">
      <div class="article-photo" role="img" aria-label="Brick ranch house with white garage"></div>
      <h3 class="article-title">Section Block Title Here</h3>
      <p class="article-text">Lorem ipsum dolor sit amet, consec tetuer adipi<br>elit, sed diam nonummy nibh euismod tincidunt<br>ut laoreet dolore magna aliquam erat volutpat.</p>
      <a class="btn btn-blue" href="#">View More</a>
    </article>
    <article class="article">
      <div class="article-photo" role="img" aria-label="Stone two-storey house with trees at dusk"></div>
      <h3 class="article-title">Section Block Title Here</h3>
      <p class="article-text">Lorem ipsum dolor sit amet, consec tetuer adipi<br>elit, sed diam nonummy nibh euismod tincidunt<br>ut laoreet dolore magna aliquam erat volutpat.</p>
      <a class="btn btn-blue" href="#">View More</a>
    </article>
    <article class="article">
      <div class="article-photo" role="img" aria-label="Single-storey cream house with green lawn"></div>
      <h3 class="article-title">Section Block Title Here</h3>
      <p class="article-text">Lorem ipsum dolor sit amet, consec tetuer adipi<br>elit, sed diam nonummy nibh euismod tincidunt<br>ut laoreet dolore magna aliquam erat volutpat.</p>
      <a class="btn btn-blue" href="#">View More</a>
    </article>
    <article class="article">
      <div class="article-photo" role="img" aria-label="Large stone house under blue sky"></div>
      <h3 class="article-title">Section Block Title Here</h3>
      <p class="article-text">Lorem ipsum dolor sit amet, consec tetuer adipi<br>elit, sed diam nonummy nibh euismod tincidunt<br>ut laoreet dolore magna aliquam erat volutpat.</p>
      <a class="btn btn-blue" href="#">View More</a>
    </article>
    <article class="article">
      <div class="article-photo" role="img" aria-label="Brick ranch house with white garage"></div>
      <h3 class="article-title">Section Block Title Here</h3>
      <p class="article-text">Lorem ipsum dolor sit amet, consec tetuer adipi<br>elit, sed diam nonummy nibh euismod tincidunt<br>ut laoreet dolore magna aliquam erat volutpat.</p>
      <a class="btn btn-blue" href="#">View More</a>
    </article>
  </section>

  <section class="closing">
    <h2 class="closing-title">GOOD PRICE, BETTER LIVING<br>FOR EVERYONE</h2>
    <p class="closing-text">Lorem ipsum dolor sit amet, consectetuer adipiscing elit, sed diam nonummy nibh euismod tincidunt ut<br>laoreet dolore magna aliquam erat volutpat. Ut wisi enim ad minim veniam,quis nostrud. Lorem ipsum<br>dolor sit amet, consectetuer adipiscing elit, sed diam.</p>
  </section>

  <footer class="footer">
    <nav class="social" aria-label="Social links">
      <a class="social-dot" href="#" aria-label="Social network one"></a>
      <a class="social-dot" href="#" aria-label="Social network two"></a>
      <a class="social-dot" href="#" aria-label="Social network three"></a>
      <a class="social-dot" href="#" aria-label="Social network four"></a>
    </nav>
    <p class="footer-text">Lorem ipsum dolor sit amet, consectetuer adipiscing elit, sed diam nonummy,<br>Lorem ipsum dolor sit amet, consectetuer.</p>
    <p class="footer-links"><a href="#">Unsubscribe</a><span class="sep">|</span><a href="#">Manage Subscriptions</a><span class="sep">|</span><a href="#">Privacy Policy</a></p>
  </footer>
</main>
</body>
</html>
```